Metal Pail and Round Tin Can Design for Resin Manufacturer

We are a fbreglass resin manufacturer located in Australia. We manufacturer resins. We are looking to have custom printed pails and can s made. We would like a innovative, and fresh design to be printed on our packaging. We would like the colours blue and white incorporated in the design. We want to show that we are a professional company with a modern touch on chemical manufacturing. Some design work will need to leave space for compliance labeling, similar to paint cans that are in many shops. Use professional paint can/pail designs as inspiration, incorporating in our current logos and design.

Target Market(s)

Fibreglass Resin Market, Fibreglass Manufacturing, Coatings

Font styles to use
Sans Serif

Colors

Designer to choose colors to be used in the design.

Requirements
Must have
• Compliance, safety information, quality ISO 9001 certification.
• The design will need to be able to be printed on several different sized cans. We would like the same consistent design on the 3 types of cans, the only changes would be the size of the product label that we would attach.
• I have attached the safety information that must be on the label. The font can be changed to match the design.
• Our 2 logos must be present on the can.
Nice to have
• A designated area to put our plain white product label. Dimension attached below.

```html
<!DOCTYPE html>
<html lang="en">
<head>
<meta charset="utf-8">
<title>Safety, Handling and Storage Label</title>
<link rel="stylesheet" href="https://fonts.googleapis.com/css2?family=Barlow+Condensed:wght@500;600;700&display=swap">
<style>
  :root {
    --page-bg: #e8ecf1;
    --label-white: #ffffff;
    --label-sky: #cfe3ee;
    --label-sky-deep: #a9cbe0;
    --paint-blue: #6f9cc4;
    --paint-blue-deep: #4f7fae;
    --ink: #2b2b2b;
    --accent-red: #d9232e;
    --roller-handle: #d9705a;
  }
  html, body {
    margin: 0;
    padding: 0;
    width: 1200px;
    height: 1200px;
    overflow: hidden;
    background: var(--page-bg);
  }
  body {
    font-family: "Barlow Condensed", "Arial Narrow", sans-serif;
    color: var(--ink);
  }
  .label {
    position: absolute;
    left: 110px;
    top: 70px;
    width: 980px;
    height: 1060px;
    background: linear-gradient(90deg, var(--label-white) 0%, var(--label-white) 30%, var(--label-sky) 70%, var(--label-sky-deep) 100%);
    overflow: hidden;
  }
  .paint-stroke {
    position: absolute;
    left: 600px;
    top: 340px;
    width: 400px;
    height: 340px;
    background: linear-gradient(90deg, rgba(111,156,196,0.2) 0%, var(--paint-blue) 35%, var(--paint-blue-deep) 100%);
    border-radius: 60px 0 0 120px;
  }
  .paint-roller {
    position: absolute;
    left: 830px;
    top: 700px;
    width: 170px;
    height: 240px;
    background: linear-gradient(160deg, var(--paint-blue-deep) 0%, var(--paint-blue) 55%, var(--roller-handle) 100%);
    border-radius: 18px;
    opacity: 0.85;
  }
  .brand {
    position: absolute;
    right: 30px;
    top: 50px;
    display: flex;
    align-items: center;
    gap: 10px;
    font-weight: 700;
    font-size: 24px;
    color: var(--paint-blue-deep);
  }
  .brand-dot {
    width: 24px;
    height: 24px;
    border-radius: 50%;
    background: var(--accent-red);
  }
  .title {
    position: absolute;
    left: 30px;
    top: 50px;
    margin: 0;
    font-weight: 700;
    font-size: 42px;
    letter-spacing: 0.5px;
  }
  .column {
    position: absolute;
    top: 120px;
    font-weight: 500;
    font-size: 22px;
    line-height: 1.2;
  }
  .column-handling { left: 30px; width: 370px; }
  .column-storage { left: 440px; width: 370px; }
  .section-heading {
    margin: 0 0 4px;
    color: var(--accent-red);
    font-weight: 600;
    font-size: 24px;
  }
  .section-heading.spaced { margin-top: 30px; }
  .rules {
    list-style: none;
    margin: 0;
    padding: 0;
  }
  .rules li {
    position: relative;
    padding-left: 14px;
    margin-bottom: 3px;
  }
  .rules li::before {
    content: "•";
    position: absolute;
    left: 0;
  }
  .warning-strip {
    position: absolute;
    left: 40px;
    bottom: 30px;
    display: flex;
    align-items: center;
    gap: 12px;
  }
  .hazard-icon {
    width: 62px;
    height: 62px;
  }
  .warning-text {
    margin-left: 12px;
    font-weight: 700;
    font-size: 24px;
  }
</style>
</head>
<body>
  <main class="label">
    <div class="paint-stroke" role="img" aria-label="Broad blue brushed paint stroke"></div>
    <div class="paint-roller" role="img" aria-label="Paint roller with orange handle"></div>

    <div class="brand"><span class="brand-dot"></span>Coralite Resins</div>

    <h1 class="title">SAFETY, HANDLING AND STORAGE</h1>

    <section class="column column-handling">
      <h2 class="section-heading">Precautions for Handling:</h2>
      <ul class="rules">
        <li>Keep out of reach of children.</li>
        <li>Read label before use.</li>
        <li>Obtain special instructions before use.</li>
        <li>Do not handle until all safety precautions have been read and understood.</li>
        <li>Keep away from heat, sparks, open flames or hot surfaces. No smoking.</li>
        <li>Keep container tightly closed.</li>
        <li>Ground, bond container and receiving equipment.</li>
        <li>Use explosion-proof electrical, ventilating and lighting.</li>
        <li>Use only non-sparking tools.</li>
        <li>Take precautionary measures against static discharge.</li>
        <li>Open slowly to control possible pressure release.</li>
        <li>Do not breathe fumes, vapours or spray.</li>
        <li>Wash hands thoroughly after handling.</li>
        <li>Do not eat, drink or smoke when using this product.</li>
        <li>Avoid release to the environment.</li>
        <li>Wear protective clothing.</li>
        <li>Use personal protective equipment as required.</li>
      </ul>
    </section>

    <section class="column column-storage">
      <h2 class="section-heading">Precautions for Storage:</h2>
      <ul class="rules">
        <li>Store away from incompatible materials. Refer to SDS.</li>
        <li>Store locked up.</li>
        <li>Store in a cool, dry place away from direct sunlight.</li>
        <li>Do not pressurize, cut, heat or weld containers - residual vapours may be flammable.</li>
        <li>This product may be flammable and will fuel a fire in progress.</li>
      </ul>
      <h2 class="section-heading spaced">First Aid</h2>
      <ul class="rules">
        <li>If swallowed DO NOT induce vomiting, rinse mouth with water and give a glass of water or milk.</li>
        <li>If vomiting occurs, keep patients head down to prevent vomit entering lungs.</li>
        <li>If splashed in eyes, flood with low pressure water for at least 15 minutes.</li>
        <li>If splashed on skin remove contaminated clothing and gently wash skin with mild soap and water. If irritating or swelling occurs, seek medical attention.</li>
        <li>Always consult medical attention or Poison Information Centre.</li>
      </ul>
    </section>

    <div class="warning-strip">
      <svg class="hazard-icon" viewBox="0 0 70 70" role="img" aria-label="Toxic hazard symbol">
        <circle cx="35" cy="35" r="31" fill="#fff" stroke="#d9232e" stroke-width="5"/>
        <circle cx="35" cy="35" r="16" fill="#3a3a3a"/>
      </svg>
      <svg class="hazard-icon" viewBox="0 0 70 70" role="img" aria-label="Keep away from children symbol">
        <circle cx="35" cy="35" r="31" fill="#fff" stroke="#d9232e" stroke-width="5"/>
        <circle cx="35" cy="35" r="16" fill="#3a3a3a"/>
        <line x1="14" y1="14" x2="56" y2="56" stroke="#d9232e" stroke-width="5"/>
      </svg>
      <span class="warning-text">KEEP OUT OF REACH OF CHILDREN</span>
    </div>
  </main>
</body>
</html>
```